Bright Valley Goods - Product Page

Looking for a design for our product pages to showcase all of the following information in an aesthetically pleasing way. <br/><br/>• Product price per piece & price breaks<br/>• Set up cost <br/>• Additional color cost<br/>• Imprint side <br/>• Product Dimensions<br/><br/>Attached are photos showing ideas we have come up with to display the information. <br/><br/>The link below shows how our product pages is currently laid out. <br/><br/>Link to webpage: https://www.brightvalleygoods.example/non-woven-reusable-promo-totes.html<br/>

Number of Pages Required

1 page

Colors
33b8a4
33a6d7
3277b5
fece3e
f9a040
a3cd3a

Requirements
Must have
• • Product price per piece & price breaks
• • Set up cost
• • Additional color cost
• • Imprint side
• • Product Dimensions

```html
<!DOCTYPE html>
<html lang="en">
<head>
<meta charset="utf-8">
<title>Bright Valley Goods – Non-Woven Reusable Promo Totes</title>
<link rel="stylesheet" href="https://fonts.googleapis.com/css2?family=Raleway:wght@400;500;600;700&family=Montserrat:wght@500;600;700&family=Cabin:wght@500;600;700&display=swap">
<style>
:root{
  --blue:#3277b5;
  --sky:#33a6d7;
  --teal:#33b8a4;
  --green:#a3cd3a;
  --yellow:#fece3e;
  --orange:#f9a040;
  --red:#e8202a;
  --ink:#222;
  --muted:#555;
  --bg:#f3f3f1;
  --line:#999;
}
*{box-sizing:border-box;margin:0;padding:0}
html,body{width:780px;height:1200px;overflow:hidden;background:var(--bg)}
body{font-family:"Raleway",sans-serif;color:var(--ink)}
.page{position:relative;width:1300px;height:2000px;transform:scale(.6);transform-origin:0 0}
.abs{position:absolute}
.breadcrumb{left:226px;top:62px;font:600 11px "Montserrat",sans-serif;color:#777}
.breadcrumb b{color:#222}
.main-card{left:100px;top:98px;width:784px;height:1792px;background:#fff;box-shadow:0 1px 4px rgba(0,0,0,.2);border-radius:3px}
.photo{border-radius:4px}
.product-title{left:391px;top:115px;font:600 16px "Montserrat",sans-serif}
.received{left:391px;top:142px;font-size:11.5px;color:var(--muted)}
.star-pill{left:391px;top:166px;width:111px;height:29px;border:2px solid var(--teal);border-radius:15px;display:flex;align-items:center;justify-content:center}
.rating-row{left:389px;width:333px;height:31px;border:2px solid var(--teal);border-radius:5px;background:#f6f6f6;display:flex;align-items:center;justify-content:space-between;padding:0 8px 0 16px;font:600 11.5px "Montserrat",sans-serif}
.stars{display:flex;gap:0}
.stars svg{fill:var(--yellow)}
.sku{left:136px;top:409px;font:600 13px "Montserrat",sans-serif;color:var(--blue)}
.sku span{color:var(--green)}
.spec-line{left:136px;top:430px;font-size:13.5px;display:flex;align-items:center;gap:6px;white-space:nowrap}
.spec-line b{font-weight:700}
.spec-line .add{color:var(--orange);font-weight:600}
.price-table{left:136px;top:464px;width:697px;border-collapse:collapse;table-layout:fixed;font-size:14px}
.price-table th{background:var(--blue);color:#fff;height:37px;font:600 14px "Raleway",sans-serif}
.price-table td{border:2px solid #aaa;text-align:center;height:38px;padding-top:4px}
.price-table td:first-child{text-align:left;padding-left:8px;font-weight:500;width:88px}
.prod-box{top:714px;width:331px;height:327px;border:2px solid var(--teal);border-radius:8px 8px 6px 6px;overflow:hidden;font-family:"Cabin",sans-serif}
.prod-head{background:var(--blue);height:69px;text-align:center;color:#fff;padding-top:8px}
.prod-head h2{font:500 26px "Cabin",sans-serif;line-height:1}
.prod-head p{color:var(--orange);font-size:14px;margin-top:14px}
.prod-band{background:var(--green);height:30px;text-align:center;font:500 24px "Cabin",sans-serif;line-height:30px;color:#222}
.prod-rows{margin-top:2px}
.prod-row{height:30px;display:flex;justify-content:space-between;align-items:center;padding:0 6px;font-size:14.5px;font-weight:500}
.prod-row span:last-child{width:88px;text-align:left}
.prod-row.hl{background:var(--blue);color:#fff}
.btn{height:36px;border-radius:3px;color:#fff;font:700 14px "Montserrat",sans-serif;display:flex;align-items:center;justify-content:center;box-shadow:0 2px 3px rgba(0,0,0,.25)}
.btn.red{background:var(--red)}
.btn.green{background:var(--green)}
.btn.yellow{background:var(--yellow)}
.sample-form{left:138px;top:1095px;width:690px;height:205px;background:var(--blue)}
.sample-form h3{position:absolute;left:0;right:0;top:16px;text-align:center;color:#fff;font:600 20px "Montserrat",sans-serif}
.field{position:absolute;width:311px;height:38px;background:#fff;border:2px solid var(--teal);border-radius:6px;font-size:14px;color:#555;padding:0 18px;display:flex;align-items:center;justify-content:space-between}
.tab{top:1310px}
.section-title{left:138px;top:1362px;font:600 18px "Montserrat",sans-serif}
.details{left:138px;top:1392px;font-size:14.5px}
.detail-row{display:flex;line-height:30px}
.detail-row dt{width:180px;font-weight:600}
.detail-row dd{width:490px;color:#444}
.features li{list-style:none;display:flex;align-items:center;gap:16px;line-height:30px}
.features svg{fill:var(--blue)}
.side-head{left:899px;width:299px;height:40px;background:var(--blue);color:#fff;border-radius:3px;font:700 13.5px "Montserrat",sans-serif;display:flex;align-items:center;justify-content:center;box-shadow:0 2px 3px rgba(0,0,0,.2)}
.rec-card{left:899px;width:299px;height:245px;background:#fff;border-radius:6px;box-shadow:0 1px 4px rgba(0,0,0,.2)}
.rec-card .photo{position:absolute;left:86px;top:4px;width:126px;height:126px}
.rec-info{position:absolute;left:0;right:0;top:144px;text-align:center;font-size:13.5px;line-height:20px}
.rec-info b{font:700 15px "Montserrat",sans-serif}
.rec-stars{display:flex;justify-content:center;align-items:center;gap:8px;margin-top:8px;color:var(--orange);font:600 13px "Montserrat",sans-serif}
.review-card{left:899px;width:299px;background:#fff;border-radius:6px;box-shadow:0 1px 4px rgba(0,0,0,.2);padding:48px 18px 10px;font-size:13.5px;line-height:20px;color:#555}
.review-card h4{text-align:center;font:600 16px "Montserrat",sans-serif;color:#222}
.review-card .stars{justify-content:center;margin:4px 0 8px}
.avatar{left:1005px;width:80px;height:80px;border-radius:50%;border:2px solid #ddd}
</style>
</head>
<body>
<svg width="0" height="0" style="position:absolute">
  <defs>
    <symbol id="star" viewBox="0 0 24 24"><path d="M12 1.8l3.1 6.6 7.2.9-5.3 5 1.4 7.1L12 17.9l-6.4 3.5 1.4-7.1-5.3-5 7.2-.9z"/></symbol>
    <symbol id="tick" viewBox="0 0 24 24"><path d="M2 13l3-3 5 5L21 2l2 2.5L10 22z"/></symbol>
  </defs>
</svg>

<div class="page">
  <div class="abs breadcrumb">Home &gt; Produxts review &gt; <b>Non-Woven Reusable Promo Totes</b></div>

  <div class="abs main-card"></div>

  <div class="abs photo" role="img" aria-label="Photo of a red and a tan non-woven promotional tote bag" style="left:135px;top:110px;width:236px;height:255px;background:linear-gradient(110deg,#d8232f 0 48%,#c9b48d 52% 100%)"></div>

  <div class="abs product-title">Non-Woven Reusable Promo Totes</div>
  <div class="abs received">Received by admin on Dec, 02, 2018</div>
  <div class="abs star-pill"><div class="stars">
    <svg width="19" height="19"><use href="#star"/></svg><svg width="19" height="19"><use href="#star"/></svg><svg width="19" height="19"><use href="#star"/></svg><svg width="19" height="19"><use href="#star"/></svg><svg width="19" height="19"><use href="#star"/></svg></div></div>

  <div class="abs rating-row" style="top:208px"><span>Customer Service</span><div class="stars"><svg width="17" height="17"><use href="#star"/></svg><svg width="17" height="17"><use href="#star"/></svg><svg width="17" height="17"><use href="#star"/></svg><svg width="17" height="17"><use href="#star"/></svg><svg width="17" height="17"><use href="#star"/></svg></div></div>
  <div class="abs rating-row" style="top:249px"><span>Customer Rating</span><div class="stars"><svg width="17" height="17"><use href="#star"/></svg><svg width="17" height="17"><use href="#star"/></svg><svg width="17" height="17"><use href="#star"/></svg><svg width="17" height="17"><use href="#star"/></svg><svg width="17" height="17"><use href="#star"/></svg></div></div>
  <div class="abs rating-row" style="top:290px"><span>Overall Rating</span><div class="stars"><svg width="17" height="17"><use href="#star"/></svg><svg width="17" height="17"><use href="#star"/></svg><svg width="17" height="17"><use href="#star"/></svg><svg width="17" height="17"><use href="#star"/></svg><svg width="17" height="17"><use href="#star"/></svg></div></div>
  <div class="abs rating-row" style="top:331px"><span>Value Rating</span><div class="stars"><svg width="17" height="17"><use href="#star"/></svg><svg width="17" height="17"><use href="#star"/></svg><svg width="17" height="17"><use href="#star"/></svg><svg width="17" height="17"><use href="#star"/></svg><svg width="17" height="17"><use href="#star"/></svg></div></div>

  <div class="abs sku">SKU: <span>PP2</span></div>
  <div class="abs spec-line"><b>Size:</b> 13" W x 14" H x 7" D &nbsp;| &nbsp;<b>Thickness:</b> 100 GSM &nbsp;&nbsp;&nbsp;
    <span class="stars"><svg width="16" height="16"><use href="#star"/></svg><svg width="16" height="16"><use href="#star"/></svg><svg width="16" height="16"><use href="#star"/></svg><svg width="16" height="16"><use href="#star"/></svg><svg width="16" height="16"><use href="#star"/></svg></span>
    <b style="font-weight:600">38 Review(s) |</b> <span class="add">Add Review</span></div>

  <table class="abs price-table">
    <tr><th colspan="8">In-Stock</th></tr>
    <tr><td>Qty</td><td>1</td><td>100+</td><td>250+</td><td>500+</td><td>1,000+</td><td>2,500+</td><td>5,000+</td></tr>
    <tr><td>Price</td><td>$0.69</td><td>$1.46</td><td>$1.35</td><td>$1.30</td><td>$1.26</td><td>$1.23</td><td>$1.19</td></tr>
    <tr><th colspan="8">Overseas</th></tr>
    <tr><td>Qty</td><td>1</td><td>1,000+</td><td>3,000+</td><td>5,000+</td><td>10,000+</td><td>25,000+</td><td>50,000+</td></tr>
    <tr><td>Price</td><td>$0.69</td><td>$1.14</td><td>$0.94</td><td>$0.89</td><td>$0.84</td><td>$0.74</td><td>$0.69</td></tr>
  </table>

  <div class="abs prod-box" style="left:138px">
    <div class="prod-head"><h2>In-Stock Production</h2><p>Orders of 288 pcs or more</p></div>
    <div class="prod-band">Includes 1 imprint Color</div>
    <div class="prod-rows">
      <div class="prod-row hl"><span>Imprint Size:</span><span>4"W x 7"H</span></div>
      <div class="prod-row"><span>Additional Colors 288 pcs:</span><span>$0.74 each</span></div>
      <div class="prod-row"><span>Additional Colors 500+ pcs:</span><span>$0.54 each</span></div>
      <div class="prod-row hl"><span>Full Color Imprint 288 pcs:</span><span>$0.99 each</span></div>
      <div class="prod-row hl"><span>Full Color Imprint 500+ pcs:</span><span>$0.79 each</span></div>
      <div class="prod-row"><span>SetUp fee:</span><span>$55 per color</span></div>
      <div class="prod-row"><span>Full Colour SetUp fee:</span><span>$95 per color</span></div>
    </div>
  </div>
  <div class="abs prod-box" style="left:500px">
    <div class="prod-head"><h2>Oversea Production</h2><p>Orders of 288 pcs or more</p></div>
    <div class="prod-band">Free 1 color, 2 Location Imprint</div>
    <div class="prod-rows">
      <div class="prod-row hl"><span>Imprint Size:</span><span>4"W x 7"H</span></div>
      <div class="prod-row"><span>Additional Colors 288 pcs:</span><span>$0.74 each</span></div>
      <div class="prod-row"><span>Additional Colors 500+ pcs:</span><span>$0.54 each</span></div>
      <div class="prod-row hl"><span>Full Color Imprint 288 pcs:</span><span>$0.99 each</span></div>
      <div class="prod-row hl"><span>Full Color Imprint 500+ pcs:</span><span>$0.79 each</span></div>
      <div class="prod-row"><span>SetUp fee:</span><span>$55 per color</span></div>
      <div class="prod-row"><span>Full Colour SetUp fee:</span><span>$95 per color</span></div>
    </div>
  </div>

  <div class="abs btn red" style="left:138px;top:1050px;width:173px">Request a Quote</div>
  <div class="abs btn green" style="left:322px;top:1050px;width:173px">Buy Now</div>
  <div class="abs btn green" style="left:506px;top:1050px;width:173px">Order Free Sample</div>

  <div class="abs sample-form">
    <h3>COMPLETE THIS FORM &amp; RECEIVE A FREE SAMPLE</h3>
    <div class="field" style="left:25px;top:55px">Name</div>
    <div class="field" style="left:354px;top:55px">Email</div>
    <div class="field" style="left:25px;top:100px">Phone Number</div>
    <div class="field" style="left:354px;top:100px">Quantity <svg width="20" height="12" viewBox="0 0 20 12"><path d="M2 2l8 8 8-8" fill="none" stroke="#a3cd3a" stroke-width="3"/></svg></div>
    <div class="btn yellow" style="position:absolute;left:258px;top:149px;width:173px">SUBMIT</div>
  </div>

  <div class="abs btn red tab" style="left:138px;width:166px">Details</div>
  <div class="abs btn green tab" style="left:312px;width:166px">Reviews</div>
  <div class="abs btn green tab" style="left:487px;width:166px">Additional Info</div>
  <div class="abs btn green tab" style="left:661px;width:167px">Shipping Estimator</div>

  <div class="abs section-title">Non-Woven Promotional Tote Bags Wholesale</div>
  <dl class="abs details">
    <div class="detail-row"><dt>Name</dt><dd>Non-Woven Reusable Promo Totes</dd></div>
    <div class="detail-row"><dt>SKU</dt><dd>PP2</dd></div>
    <div class="detail-row"><dt>Size</dt><dd>13" W x 14" H x 7" D</dd></div>
    <div class="detail-row"><dt>Thickness</dt><dd>100 GSM</dd></div>
    <div class="detail-row"><dt>Available Colors</dt><dd>Black, Hunter Green, Kelly Green, Lime Green, MauibBlue, Navy Blue, Purple, Red, Royal Blue, Tan, Teal &amp; Yellow</dd></div>
    <div class="detail-row"><dt>Imprint Area</dt><dd>8" W x 8" H</dd></div>
    <div class="detail-row"><dt>Key Features</dt><dd>
      <ul class="features">
        <li><svg width="20" height="20"><use href="#tick"/></svg>Spacious Main Compartment, 1274 Cubic Inches</li>
        <li><svg width="20" height="20"><use href="#tick"/></svg>22" Carry Straps</li>
        <li><svg width="20" height="20"><use href="#tick"/></svg>Made from 100 GSM Non-Woven Polypropylene</li>
        <li><svg width="20" height="20"><use href="#tick"/></svg>Eco-Friendly and 100% Recyclable</li>
        <li><svg width="20" height="20"><use href="#tick"/></svg>Removable Hard Bottom Insert at the Base</li>
        <li><svg width="20" height="20"><use href="#tick"/></svg>5 Day Standard Production / RUSH service available</li>
        <li><svg width="20" height="20"><use href="#tick"/></svg>10 Day Production for Full Color Artwork</li>
        <li><svg width="20" height="20"><use href="#tick"/></svg>8" Wide x 8" High Imprint Area</li>
        <li><svg width="20" height="20"><use href="#tick"/></svg>Made From Recycled Content</li>
      </ul></dd></div>
  </dl>

  <div class="abs side-head" style="top:98px">RECOMMENDED PRODUCTS</div>

  <div class="abs rec-card" style="top:148px">
    <div class="photo" role="img" aria-label="Photo of a blue and a red promotional tote bag" style="background:linear-gradient(110deg,#1f7fc0 0 48%,#d9242e 52%)"></div>
    <div class="rec-info"><b>Size:</b> 13" W x 15" H x 10" D<br><b>As Low As:</b> $0.74<br><b>SKU:</b>PP3A
      <div class="rec-stars"><span class="stars"><svg width="16" height="16"><use href="#star"/></svg><svg width="16" height="16"><use href="#star"/></svg><svg width="16" height="16"><use href="#star"/></svg><svg width="16" height="16"><use href="#star"/></svg><svg width="16" height="16"><use href="#star"/></svg></span>30 Reviews</div></div>
  </div>
  <div class="abs rec-card" style="top:404px">
    <div class="photo" role="img" aria-label="Photo of a green and a red promotional tote bag" style="background:linear-gradient(110deg,#3fd14a 0 50%,#e23a2c 54%)"></div>
    <div class="rec-info"><b>Size:</b> 16" W x 12" H x 6" D<br><b>As Low As:</b> $0.54<br><b>SKU:</b>PP9
      <div class="rec-stars"><span class="stars"><svg width="16" height="16"><use href="#star"/></svg><svg width="16" height="16"><use href="#star"/></svg><svg width="16" height="16"><use href="#star"/></svg><svg width="16" height="16"><use href="#star"/></svg><svg width="16" height="16"><use href="#star"/></svg></span>20 Reviews</div></div>
  </div>
  <div class="abs rec-card" style="top:660px">
    <div class="photo" role="img" aria-label="Photo of a purple and a tan promotional tote bag" style="background:linear-gradient(110deg,#6a4aa8 0 48%,#e3c9a0 52%)"></div>
    <div class="rec-info"><b>Size:</b> 13" W x 15" H x 10" D<br><b>As Low As:</b> $0.69<br><b>SKU:</b>PP21A
      <div class="rec-stars"><span class="stars"><svg width="16" height="16"><use href="#star"/></svg><svg width="16" height="16"><use href="#star"/></svg><svg width="16" height="16"><use href="#star"/></svg><svg width="16" height="16"><use href="#star"/></svg><svg width="16" height="16"><use href="#star"/></svg></span>23 Reviews</div></div>
  </div>

  <div class="abs side-head" style="top:916px">RECENT REVIEW</div>

  <div class="abs review-card" style="top:1002px;height:187px">
    <h4>Martin L</h4>
    <div class="stars"><svg width="22" height="22"><use href="#star"/></svg><svg width="22" height="22"><use href="#star"/></svg><svg width="22" height="22"><use href="#star"/></svg><svg width="22" height="22"><use href="#star"/></svg><svg width="22" height="22"><use href="#star"/></svg></div>
    <p>Great product. I really am amazed and impressed with this company. They were very patient when assisting me find this item.</p>
  </div>
  <div class="abs avatar" role="img" aria-label="Reviewer portrait photo" style="top:965px;background:linear-gradient(160deg,#8a8f94,#3b3e42)"></div>

  <div class="abs review-card" style="top:1237px;height:212px">
    <h4>Helena R</h4>
    <div class="stars"><svg width="22" height="22"><use href="#star"/></svg><svg width="22" height="22"><use href="#star"/></svg><svg width="22" height="22"><use href="#star"/></svg><svg width="22" height="22"><use href="#star"/></svg><svg width="22" height="22"><use href="#star"/></svg></div>
    <p>Outstanding!!! These bags were recom-mended to us by another company, and they came out amazing!!! The ordering process was so easy, and the imprint came out better than we expected...</p>
  </div>
  <div class="abs avatar" role="img" aria-label="Reviewer portrait photo" style="top:1200px;background:linear-gradient(160deg,#c9c9c9,#4a3c36)"></div>

  <div class="abs btn yellow" style="left:961px;top:1470px;width:175px">View More</div>
</div>
</body>
</html>
```